The Copper Lantern Business Cards

We are a Craft Beer/Upscale dining Bar/Restaurant. We'll have 24 taps of craft beers and several types of bottled beers. In addition, we'll be serving a variety of top shelf bourbons, spirits and wines with a small unique menu. I'd like the design to be sophisticated, elegant and modern while staying away from "cartoonish" pictures.
Updates
Hello, I've added some example logos for inspiration. I'd like to use a lot of black/white with maybe a little color for a "pop". Thank you!
Industry/Entity Type
Business
Contact Information for Business Card
THE COPPER LANTERN
Marco Dellarosa
592 Wexley Street
Norfolk, Virginia 23847
Office: (757) 555-0148
Mobile: (757) 555-0193
Look and feel

```html
<!DOCTYPE html>
<html lang="en">
<head>
<meta charset="utf-8">
<title>The Copper Lantern — Business Card</title>
<link href="https://fonts.googleapis.com/css2?family=Questrial&display=swap" rel="stylesheet">
<style>
  :root {
    --backdrop: #d8d5d0;
    --card-top: #1b1b1b;
    --card-bottom: #0c0c0c;
    --silver: #e4e4e4;
    --silver-soft: #b9b9b9;
    --rule: #9a9a9a;
  }
  * { margin: 0; padding: 0; box-sizing: border-box; }
  html, body {
    width: 1200px;
    height: 864px;
    overflow: hidden;
    background: var(--backdrop);
    font-family: "Questrial", "Century Gothic", sans-serif;
  }
  .stage {
    width: 1200px;
    height: 864px;
    display: flex;
    align-items: center;
    justify-content: center;
  }
  .business-card {
    position: relative;
    width: 460px;
    height: 800px;
    background: linear-gradient(160deg, var(--card-top), var(--card-bottom));
    color: var(--silver);
    box-shadow: 0 10px 30px rgba(0,0,0,0.25);
  }
  .card-frame {
    position: absolute;
    inset: 0;
    width: 100%;
    height: 100%;
  }
  .brand-mark {
    position: absolute;
    top: 140px;
    left: 60px;
    right: 60px;
    text-align: center;
    font-size: 26px;
    letter-spacing: 1.5px;
    white-space: nowrap;
    color: var(--silver);
  }
  .contact-block {
    position: absolute;
    top: 300px;
    left: 60px;
    right: 60px;
    text-align: center;
  }
  .person-name {
    font-size: 38px;
    font-weight: 400;
    letter-spacing: 0.5px;
    white-space: nowrap;
    padding-bottom: 12px;
    border-bottom: 2px solid var(--rule);
  }
  .address {
    margin-top: 16px;
    font-size: 22px;
    line-height: 1.35;
    color: var(--silver-soft);
  }
  .phones {
    margin-top: 14px;
    font-size: 24px;
    line-height: 1.4;
    padding-bottom: 16px;
    border-bottom: 2px solid var(--rule);
  }
  .tagline {
    position: absolute;
    top: 590px;
    left: 50px;
    right: 50px;
    text-align: center;
    font-size: 16px;
    letter-spacing: 1.5px;
    line-height: 1.6;
    font-weight: 700;
    color: var(--silver);
  }
</style>
</head>
<body>
  <main class="stage">
    <article class="business-card">
      <svg class="card-frame" viewBox="0 0 460 800" aria-hidden="true">
        <rect x="26" y="26" width="408" height="748" fill="none" stroke="var(--silver)" stroke-width="5" stroke-dasharray="4 4"/>
        <rect x="33" y="33" width="394" height="734" fill="none" stroke="var(--silver-soft)" stroke-width="1"/>
      </svg>

      <div class="brand-mark">THE COPPER LANTERN</div>

      <section class="contact-block">
        <h1 class="person-name">Marco Dellarosa</h1>
        <p class="address">592 Wexley Street<br>Norfolk, Virginia 23847</p>
        <p class="phones">Office: (757) 555-0148<br>Mobile: (757) 555-0193</p>
      </section>

      <p class="tagline">CRAFT BEER | UPSCALE DINING BAR<br>RESTAURANT</p>
    </article>
  </main>
</body>
</html>
```